1 Cup Pod - Regular and Decaf

I am looking for 2 package designs. When you open the uploaded file it show one for regular and one for decaf. The size is also on the example template. Both products with still be named Café Brisa, only things we are looking for is new colors and design of package. you can use up to 4 colors at this time.

We are open to all types of ideas and colors. the only thins is the regular and decaf must be different colors.

Requirements
Must have
• Must use the exact information used on front and back of both package design from the example template. The only thing is to add, 75702 next to where it says Tyler, TX

```html
<!DOCTYPE html>
<html lang="en">
<head>
<meta charset="utf-8">
<title>Café Brisa – Single-Cup Coffee Pod Packages</title>
<link rel="stylesheet" href="https://fonts.googleapis.com/css2?family=PT+Sans:wght@400;700&display=swap">
<style>
  :root {
    --page: #ffffff;
    --gold: #f2c14e;
    --white: #ffffff;
    --regular-back: #43170a;
    --regular-edge: #8a4a22;
    --regular-deep: #2a0c04;
    --decaf-back: #4b3303;
    --decaf-edge: #a88a1c;
    --decaf-deep: #3a2702;
    --red-back: #560207;
    --red-edge: #b0222a;
    --red-deep: #3f0104;
  }
  * { box-sizing: border-box; margin: 0; padding: 0; }
  html, body {
    width: 803px; height: 1200px; overflow: hidden;
    background: var(--page);
    font-family: "PT Sans", Arial, sans-serif;
  }
  .sheet { position: relative; width: 803px; height: 1200px; }
  .package {
    position: absolute; left: 78px; width: 633px; height: 323px;
    display: flex;
  }
  .package--regular { top: 77px; }
  .package--decaf-gold { top: 439px; }
  .package--decaf-red { top: 803px; }

  .front {
    position: relative; width: 317px; height: 100%;
    color: var(--white); text-align: center;
  }
  .front-image { position: absolute; inset: 0; }
  .package--regular .front-image {
    background: radial-gradient(circle at 50% 50%, var(--regular-deep) 0%, var(--regular-edge) 100%);
  }
  .package--decaf-gold .front-image {
    background: radial-gradient(circle at 50% 50%, var(--decaf-deep) 0%, var(--decaf-edge) 100%);
  }
  .package--decaf-red .front-image {
    background: radial-gradient(circle at 50% 50%, var(--red-deep) 0%, var(--red-edge) 100%);
  }
  .front-content {
    position: relative; height: 100%;
    display: flex; flex-direction: column; align-items: center;
    padding-top: 44px;
  }
  .brand-dot {
    width: 34px; height: 34px; border-radius: 50%;
    background: var(--gold); margin-bottom: 40px;
  }
  .brand-name {
    font-weight: 700; color: var(--gold);
    font-size: 54px; line-height: 52px; letter-spacing: 1px;
    text-transform: uppercase;
  }
  .product-line {
    margin-top: 14px; font-size: 11.5px; font-weight: 700; line-height: 12px;
  }
  .product-variant {
    font-size: 16px; font-weight: 700; letter-spacing: 0.5px; margin-top: 4px;
  }
  .divider {
    margin-top: 14px; width: 108px; height: 3px; background: var(--gold);
    border-radius: 2px;
  }

  .back {
    width: 316px; height: 100%;
    display: flex; flex-direction: column; align-items: center;
    padding-top: 96px; text-align: center; color: var(--white);
  }
  .package--regular .back { background: var(--regular-back); }
  .package--decaf-gold .back { background: var(--decaf-back); }
  .package--decaf-red .back { background: var(--red-back); }
  .directions { font-size: 11.5px; line-height: 11.5px; }
  .directions strong { font-weight: 700; display: block; }
  .maker {
    margin-top: 12px; color: var(--gold); font-weight: 700;
    font-size: 14.5px; line-height: 17px;
  }
</style>
</head>
<body>
<main class="sheet">

  <section class="package package--regular">
    <div class="front">
      <div class="front-image" role="img" aria-label="Photograph of a swirling coffee surface in brown tones"></div>
      <div class="front-content">
        <div class="brand-dot"></div>
        <div class="brand-name">Café<br>Brisa</div>
        <p class="product-line">Single-Cup Coffee Pod<br>Colombian 7g</p>
        <p class="product-variant">REGULAR</p>
        <div class="divider"></div>
      </div>
    </div>
    <div class="back">
      <p class="directions"><strong>DIRECTIONS:</strong>Carefully open package.<strong>DO NOT OPEN FILTER PACK</strong>Place single-cup coffee pod<br>in brew basket or funnel.<br>Follow the directions<br>on coffee maker.</p>
      <p class="maker">MARLOW &amp; SONS<br>Millbrook, Texas 75790</p>
    </div>
  </section>

  <section class="package package--decaf-gold">
    <div class="front">
      <div class="front-image" role="img" aria-label="Photograph of a swirling coffee surface in golden tones"></div>
      <div class="front-content">
        <div class="brand-dot"></div>
        <div class="brand-name">Café<br>Brisa</div>
        <p class="product-line">Single-Cup Coffee Pod<br>Colombian 7g</p>
        <p class="product-variant">DECAFFEINATED</p>
        <div class="divider"></div>
      </div>
    </div>
    <div class="back">
      <p class="directions"><strong>DIRECTIONS:</strong>Carefully open package.<strong>DO NOT OPEN FILTER PACK</strong>Place single-cup coffee pod<br>in brew basket or funnel.<br>Follow the directions<br>on coffee maker.</p>
      <p class="maker">MARLOW &amp; SONS<br>Millbrook, Texas 75790</p>
    </div>
  </section>

  <section class="package package--decaf-red">
    <div class="front">
      <div class="front-image" role="img" aria-label="Photograph of a swirling coffee surface in red tones"></div>
      <div class="front-content">
        <div class="brand-dot"></div>
        <div class="brand-name">Café<br>Brisa</div>
        <p class="product-line">Single-Cup Coffee Pod<br>Colombian 7g</p>
        <p class="product-variant">DECAFFEINATED</p>
        <div class="divider"></div>
      </div>
    </div>
    <div class="back">
      <p class="directions"><strong>DIRECTIONS:</strong>Carefully open package.<strong>DO NOT OPEN FILTER PACK</strong>Place single-cup coffee pod<br>in brew basket or funnel.<br>Follow the directions<br>on coffee maker.</p>
      <p class="maker">MARLOW &amp; SONS<br>Millbrook, Texas 75790</p>
    </div>
  </section>

</main>
</body>
</html>
```